Dental specialist needs a sharp looking letterhead

I am looking for a letterhead to be used to send letters and communication between myself (a dental specialist) and other dentists.
My office is a state of the art dental specialty office.
I need to letterhead to also state:
Derek L. Halvorsen DDS
2847 Birchmont Avenue, Suite K
West Larkdale, NY 14390
(716)555-0193
fax: (716)555-0157
halvorsenpulp.com (**this email address may change)

i included my logo designs.
thank you

Target Market(s)

dentists

Industry/Entity Type

Communication

Requirements
Must have
• the included logo, whether the vertical or horizontal versions

```html
<!DOCTYPE html>
<html lang="en">
<head>
<meta charset="utf-8">
<title>Birchmont Endodontics Letterhead</title>
<link href="https://fonts.googleapis.com/css2?family=Roboto+Slab:wght@300;400;600&display=swap" rel="stylesheet">
<style>
  :root {
    --sky: #42a5dc;
    --leaf: #8dc63f;
    --ink: #111111;
    --text: #333333;
    --paper: #ffffff;
  }
  * { margin: 0; padding: 0; box-sizing: border-box; }
  html, body { width: 931px; height: 1200px; overflow: hidden; background: var(--paper); }
  .letterhead {
    position: relative;
    width: 931px;
    height: 1200px;
    background: var(--paper);
    font-family: "Roboto Slab", serif;
    color: var(--text);
  }
  .header-art { position: absolute; left: 0; top: 0; }
  .doctor {
    position: absolute;
    left: 560px; width: 250px; top: 12px;
    text-align: center;
    color: var(--paper);
  }
  .doctor-name { font-size: 20px; font-weight: 400; line-height: 28px; }
  .doctor-phone { font-size: 15px; font-weight: 300; line-height: 22px; margin-top: 6px; }
  .doctor-phone svg { vertical-align: -2px; margin-right: 4px; }
  .brand {
    position: absolute;
    left: 70px; top: 100px;
    display: flex; align-items: center;
  }
  .brand-dot {
    width: 56px; height: 56px; border-radius: 50%;
    background: var(--sky);
    margin-right: 14px;
  }
  .brand-rule { width: 1px; height: 90px; background: var(--ink); margin-right: 9px; }
  .brand-name {
    font-weight: 600;
    color: var(--ink);
    line-height: 1;
  }
  .brand-name .line-main { display: block; font-size: 33px; letter-spacing: -0.5px; }
  .brand-name .line-sub { display: block; font-size: 13px; letter-spacing: 2px; margin-top: 6px; padding-left: 26px; }
  .footer-contact {
    position: absolute;
    left: 36px; top: 1126px;
    display: flex; align-items: center;
    font-size: 15px; font-weight: 300;
  }
  .contact-list { list-style: none; }
  .contact-list li { display: flex; align-items: center; height: 21px; }
  .contact-list svg { width: 16px; margin-right: 8px; }
  .footer-rule { width: 1px; height: 36px; background: var(--text); margin: 0 18px 0 14px; }
  .address { display: flex; align-items: center; font-size: 17px; font-weight: 400; }
  .address svg { margin-right: 11px; }
</style>
</head>
<body>
<div class="letterhead">
  <svg class="header-art" width="931" height="300" viewBox="0 0 931 300" aria-hidden="true">
    <path d="M0,0 H931 L925,10 C850,70 720,92 560,82 C430,72 330,38 230,44 C120,50 40,110 0,190 Z" fill="var(--sky)"/>
    <path d="M0,210 C40,120 120,62 230,52 C330,44 430,80 560,92 C720,104 850,80 922,14" fill="none" stroke="var(--paper)" stroke-width="16"/>
    <path d="M2,215 C40,125 120,66 230,57 C330,49 430,84 560,96 C720,108 850,84 918,20" fill="none" stroke="var(--leaf)" stroke-width="9"/>
    <path d="M0,262 C5,180 70,105 170,80 C270,60 370,74 440,92 C360,82 260,76 180,94 C90,120 30,190 2,262 Z" fill="var(--ink)"/>
  </svg>

  <div class="doctor">
    <p class="doctor-name">Derek L. Halvorsen, DDS</p>
    <p class="doctor-phone"><svg width="13" height="13" viewBox="0 0 24 24"><path d="M6.6 10.8a15 15 0 0 0 6.6 6.6l2.2-2.2a1 1 0 0 1 1-.25 11.4 11.4 0 0 0 3.6.57 1 1 0 0 1 1 1V20a1 1 0 0 1-1 1A17 17 0 0 1 3 4a1 1 0 0 1 1-1h3.5a1 1 0 0 1 1 1c0 1.25.2 2.45.57 3.57a1 1 0 0 1-.25 1z" fill="none" stroke="currentColor" stroke-width="1.8"/></svg>716-555-0193</p>
  </div>

  <div class="brand">
    <div class="brand-dot"></div>
    <div class="brand-rule"></div>
    <p class="brand-name"><span class="line-main">BIRCHMONT</span><span class="line-sub">Endodontics P.C.</span></p>
  </div>

  <div class="footer-contact">
    <ul class="contact-list">
      <li><svg viewBox="0 0 24 24" height="16"><path d="M6.6 10.8a15 15 0 0 0 6.6 6.6l2.2-2.2a1 1 0 0 1 1-.25 11.4 11.4 0 0 0 3.6.57 1 1 0 0 1 1 1V20a1 1 0 0 1-1 1A17 17 0 0 1 3 4a1 1 0 0 1 1-1h3.5a1 1 0 0 1 1 1c0 1.25.2 2.45.57 3.57a1 1 0 0 1-.25 1z" fill="var(--leaf)"/></svg>716-555-0157</li>
      <li><svg viewBox="0 0 24 24" height="14"><rect x="2" y="5" width="20" height="14" fill="var(--sky)"/><path d="M2 5l10 8 10-8" fill="none" stroke="var(--paper)" stroke-width="1.6"/></svg>halvorsenpulp@mailbox.com</li>
    </ul>
    <div class="footer-rule"></div>
    <p class="address"><svg width="14" height="20" viewBox="0 0 14 20"><path d="M7 0a7 7 0 0 0-7 7c0 5 7 13 7 13s7-8 7-13a7 7 0 0 0-7-7zm0 9.5A2.5 2.5 0 1 1 7 4.5a2.5 2.5 0 0 1 0 5z" fill="var(--text)"/></svg>2847 Birchmont Avenue, Suite K, West Larkdale, NY 14390</p>
  </div>
</div>
</body>
</html>
```